'Halbrook Video' - Website Template Design (that I can use in Word Press)

I would like a professional, colorful website template (4 pages) designed in a format that can be used with Word Press. Upon completion of the design, I would like to take over and maintain/host using Web Press and my Net Parrot account.

My business is videography - producing videos for companies, organizations and not-for-profit charities. Our company will do everything, including writing, planning, producing, directing filming and editing videos etc.

I have a colorful logo and business card already designed and I would like the website built around the look of the logo and business card.

I would like an index page designed first. Once the designer has created an index page I like best, I would like three more pages created with that same design.

1) A 'contact us' page
2) A page with a plug in that would allow me to upload video or connect to ClipVane to show samples of my videography
3) A general template page I could add new pages to in the future.

Target Market(s)

businesses of all kinds, organizations, governments, not-for-profit charities

Industry/Entity Type

Film Production

Number of Pages Required

4 page

Font styles to use
Sans Serif

Requirements
Must have
• 1) Index page
• 2) Contact Us page
• 2) A page with a plug in that would allow me to upload video or connect to ClipVane to show samples of my videography
• 3) A general template page I could add new pages to in the future
Nice to have
• Surprise me! I love lots of color and am open to creative ideas.

```html
<!DOCTYPE html>
<html lang="en">
<head>
<meta charset="utf-8">
<title>Halbrook Video</title>
<link href="https://fonts.googleapis.com/css2?family=Lato:wght@400;700;900&display=swap" rel="stylesheet">
<style>
:root{
  --ink:#1b1b1b;
  --purple:#7b3f98;
  --red:#e0202a;
  --green:#8cc63f;
  --blue:#2b4ea2;
  --orange:#f26522;
  --paper:#f2f2f2;
  --footer:#242424;
  --footer-deep:#111;
  --muted:#9a9a9a;
}
*{box-sizing:border-box;margin:0;padding:0}
html,body{width:1200px;height:2174px;overflow:hidden}
body{font-family:"Lato",Arial,sans-serif;background:var(--paper);color:var(--ink);position:relative}
.abs{position:absolute}

/* header */
.site-header{position:absolute;left:0;top:0;width:1200px;height:116px;background:#fff}
.brand{position:absolute;left:160px;top:30px;display:flex;align-items:center;gap:10px}
.brand-mark{width:22px;height:22px;background:var(--red)}
.brand-name{font-weight:900;font-size:22px;letter-spacing:1px;color:var(--ink)}
.top-contact{position:absolute;right:162px;top:24px;display:flex;align-items:center;gap:8px;font-size:14px;font-weight:700}
.top-contact .phone{margin-right:10px;display:flex;align-items:center;gap:6px}
.social{display:flex;gap:6px}
.social span{width:22px;height:22px;display:block}
.s1{background:#3b5998}.s2{background:#1da1f2}.s3{background:#0e76a8}.s4{background:#dd4b39}
.top-rule{position:absolute;left:797px;top:63px;width:241px;height:1px;background:#ddd}
.main-nav{position:absolute;right:162px;top:82px;display:flex;gap:36px;font-size:15px;font-weight:700;text-transform:uppercase}
.main-nav a{text-decoration:none}
.n-home{color:var(--ink)}.n-about{color:var(--purple)}.n-services{color:var(--red)}.n-gallery{color:var(--green)}.n-contact{color:var(--blue)}

/* hero */
.hero{position:absolute;left:0;top:116px;width:1200px;height:485px;background:#0c0c0c}
.hero-photo{position:absolute;left:0;top:8px;width:1200px;height:469px;
  background:radial-gradient(ellipse at 30% 40%,#5a4a45 0%,#2e2422 45%,#130f0e 100%)}
.perf{position:absolute;left:0;width:1200px;height:8px;
  background:radial-gradient(circle,#fff 1.6px,transparent 2px) 0 0/7px 8px,#000}
.perf.top{top:0}.perf.bottom{bottom:0}
.hero-box{position:absolute;left:160px;top:195px;width:562px;height:186px;background:rgba(40,40,40,.6);text-align:center;color:#fff}
.hero-box h1{font-size:24px;font-weight:700;line-height:33px;text-transform:uppercase;margin-top:26px}
.slider-dots{display:flex;justify-content:center;gap:8px;margin-top:16px}
.slider-dots span{width:12px;height:12px}

/* welcome */
.welcome{position:absolute;left:0;top:601px;width:1200px;height:320px;text-align:center}
.welcome-mark{width:60px;height:60px;background:var(--orange);margin:37px auto 10px}
.welcome h2{font-size:19px;font-weight:700;line-height:22px}
.welcome .wordmark{font-size:33px;font-weight:900;letter-spacing:1px;line-height:40px}
.welcome p{width:890px;margin:24px auto 0;font-size:12.6px;line-height:21.7px;color:#333}

/* services */
.services{position:absolute;left:0;top:921px;width:1200px;height:487px;overflow:hidden;
  background:linear-gradient(135deg,#2a2313 0%,#0d0d12 35%,#1b0f1d 65%,#0e1a12 100%)}
.section-title{position:absolute;left:160px;width:878px;display:flex;align-items:center;gap:20px;font-size:27px;font-weight:700;text-transform:uppercase}
.section-title::before,.section-title::after{content:"";flex:1;height:1px}
.services .section-title{top:34px;color:#fff}
.services .section-title::before,.services .section-title::after{background:#555}
.ring{position:absolute;left:354px;top:182px;width:492px;height:492px;border:5px solid #fff;border-radius:50%}
.center-name{position:absolute;left:500px;top:327px;width:200px;text-align:center;color:#fff;font-weight:900;font-size:26px;line-height:32px;letter-spacing:1px}
.svc-box{position:absolute;width:106px;height:98px;background:#f7f7f7;display:flex;align-items:center;justify-content:center}
.svc-label{position:absolute;font-size:14px;font-weight:700;text-transform:uppercase}

/* gallery */
.gallery{position:absolute;left:0;top:1408px;width:1200px;height:479px}
.gallery .section-title{top:40px;color:var(--ink)}
.gallery .section-title::before,.gallery .section-title::after{background:#ddd}
.video-card{position:absolute;top:118px;width:414px}
.video-card h3{font-size:20px;font-weight:700;color:var(--purple);text-transform:uppercase;margin-bottom:12px;white-space:nowrap}
.video-frame{border:3px solid #ddd;background:#fff;padding:3px;height:234px}
.video-thumb{position:relative;height:222px}
.v1{background:linear-gradient(120deg,#6f8a3c 0%,#3e4d25 50%,#15150f 100%)}
.v2{background:linear-gradient(120deg,#cfc7b6 0%,#7b7468 50%,#2a2e3a 100%)}
.play{position:absolute;left:50%;top:50%;width:36px;height:36px;margin:-18px 0 0 -18px;background:rgba(230,230,230,.85)}
.play::after{content:"";position:absolute;left:14px;top:11px;border-left:11px solid #333;border-top:7px solid transparent;border-bottom:7px solid transparent}
.gallery-dots{position:absolute;top:432px;left:0;width:1200px;display:flex;justify-content:center;gap:6px}
.gallery-dots span{width:7px;height:7px;border-radius:50%;background:#ccc}
.gallery-dots .on{background:var(--green)}

/* footer */
.site-footer{position:absolute;left:0;top:1887px;width:1200px;height:249px;background:var(--footer);color:#fff}
.f-col{position:absolute;top:40px}
.f-col h4{font-size:13px;font-weight:700;text-transform:uppercase;padding-bottom:6px;border-bottom:1px solid #444}
.quick{left:162px;width:110px}
.quick ul{list-style:none;margin-top:10px}
.quick li{font-size:11px;line-height:32.5px;text-transform:uppercase;padding-left:10px;position:relative}
.quick li::before{content:"";position:absolute;left:0;top:14px;width:5px;height:5px;background:#ccc}
.contact{left:343px;width:175px;font-size:11px}
.contact .org{font-weight:700;margin-top:12px}
.contact .addr{line-height:15px}
.contact .row{display:flex;align-items:center;gap:8px;margin-top:18px}
.mapcol{left:588px;width:247px}
.map{margin-top:12px;width:247px;height:147px;background:linear-gradient(135deg,#e9e5dc,#d8dfe6 60%,#f0d9a6)}
.f-brand{position:absolute;left:900px;top:86px;width:144px;text-align:center}
.f-brand .mark{width:30px;height:30px;background:var(--orange);margin:0 auto 10px}
.f-brand .name{font-size:20px;font-weight:900;letter-spacing:1px}
.f-brand .social{justify-content:center;margin-top:22px}
.copyright{position:absolute;left:0;top:2136px;width:1200px;height:38px;background:var(--footer-deep);color:#ddd;font-size:11px;line-height:38px;text-align:center;text-transform:uppercase}
</style>
</head>
<body>

<header class="site-header">
  <div class="brand"><span class="brand-mark"></span><span class="brand-name">HALBROOK VIDEO</span></div>
  <div class="top-contact">
    <span class="phone">
      <svg width="18" height="18" viewBox="0 0 24 24"><path d="M6.6 10.8a15 15 0 006.6 6.6l2.2-2.2a1 1 0 011-.25 11.4 11.4 0 003.6.6 1 1 0 011 1V20a1 1 0 01-1 1A17 17 0 013 4a1 1 0 011-1h3.5a1 1 0 011 1c0 1.25.2 2.45.6 3.6a1 1 0 01-.25 1z" fill="none" stroke="#222" stroke-width="1.6"/></svg>
      123-456-7890
    </span>
    <div class="social" aria-label="Social links"><span class="s1"></span><span class="s2"></span><span class="s3"></span><span class="s4"></span></div>
  </div>
  <div class="top-rule"></div>
  <nav class="main-nav">
    <a class="n-home">Home</a><a class="n-about">About Us</a><a class="n-services">Services</a><a class="n-gallery">Video Gallery</a><a class="n-contact">Contact Us</a>
  </nav>
</header>

<section class="hero">
  <div class="perf top"></div>
  <div class="hero-photo" role="img" aria-label="Interview being filmed in a studio with a video camera on a tripod in the foreground"></div>
  <div class="perf bottom"></div>
  <div class="hero-box">
    <h1>Our business is producing<br>videos for companies, organizations<br>and not-for-profit charities</h1>
    <div class="slider-dots">
      <span style="background:var(--purple)"></span>
      <span style="border:2px solid var(--orange)"></span>
      <span style="background:var(--green)"></span>
      <span style="background:var(--blue)"></span>
    </div>
  </div>
</section>

<section class="welcome">
  <div class="welcome-mark"></div>
  <h2>WELCOME TO</h2>
  <div class="wordmark">HALBROOK VIDEO</div>
  <p>Lorem ipsum dolor sit amet, consectetuer adipiscing elit, sed diam nonummy nibh euismod tincidunt ut laoreet dolore magna aliquam erat volutpat. Ut wisi enim ad minim veniam, quis nostrud exerci tation ullamcorper suscipit lobortis nisl ut aliquip ex ea commodo consequat. Duis autem vel eum iriure dolor in hendrerit in vulputate velit esse molestie consequat, vel illum dolore eu feugiat nulla facilisis at vero eros et accumsan et iusto odio dignissim qui blandit praesent luptatum zzril delenit augue duis dolore te feugait nulla facilisi.</p>
</section>

<section class="services">
  <div class="section-title">Our Services</div>
  <div class="ring"></div>
  <div class="center-name">HALBROOK<br>VIDEO</div>

  <div class="svc-label" style="left:550px;top:96px;width:106px;text-align:center;color:var(--red)">Producing</div>
  <div class="svc-box" style="left:550px;top:131px">
    <svg width="54" height="44" viewBox="0 0 54 44"><circle cx="12" cy="10" r="7" fill="none" stroke="#e0202a" stroke-width="4"/><circle cx="28" cy="10" r="7" fill="none" stroke="#e0202a" stroke-width="4"/><rect x="4" y="20" width="32" height="20" rx="3" fill="#e0202a"/><path d="M36 26l14-7v22l-14-7z" fill="#e0202a"/></svg>
  </div>

  <div class="svc-label" style="left:253px;top:237px;color:var(--purple)">Planning</div>
  <div class="svc-box" style="left:353px;top:196px">
    <svg width="54" height="50" viewBox="0 0 54 50"><rect x="4" y="8" width="36" height="36" fill="none" stroke="#7b3f98" stroke-width="4"/><path d="M12 36l8-12 8 12z" fill="#7b3f98"/><rect x="12" y="14" width="8" height="8" fill="#7b3f98"/><path d="M28 30l18-20 5 5-18 20-7 2z" fill="#7b3f98"/></svg>
  </div>

  <div class="svc-label" style="left:874px;top:237px;color:var(--blue)">Directing Filming</div>
  <div class="svc-box" style="left:745px;top:196px">
    <svg width="50" height="46" viewBox="0 0 50 46"><path d="M4 14L42 4l2 8L6 22z" fill="#2b4ea2"/><rect x="5" y="22" width="40" height="22" rx="2" fill="#2b4ea2"/><rect x="10" y="28" width="30" height="3" fill="#fff"/><rect x="10" y="35" width="30" height="3" fill="#fff"/></svg>
  </div>

  <div class="svc-label" style="left:222px;top:385px;color:var(--green)">Writing</div>
  <div class="svc-box" style="left:308px;top:344px">
    <svg width="44" height="54" viewBox="0 0 44 54"><rect x="4" y="6" width="36" height="44" rx="4" fill="none" stroke="#8cc63f" stroke-width="4"/><rect x="14" y="2" width="16" height="8" fill="#8cc63f"/><rect x="11" y="18" width="22" height="3" fill="#8cc63f"/><rect x="11" y="26" width="22" height="3" fill="#8cc63f"/><rect x="11" y="34" width="22" height="3" fill="#8cc63f"/><rect x="11" y="42" width="14" height="3" fill="#8cc63f"/></svg>
  </div>

  <div class="svc-label" style="left:919px;top:385px;color:var(--orange)">Editing Videos</div>
  <div class="svc-box" style="left:790px;top:344px">
    <svg width="54" height="48" viewBox="0 0 54 48"><rect x="4" y="14" width="32" height="30" fill="none" stroke="#f26522" stroke-width="4"/><rect x="4" y="14" width="7" height="30" fill="#f26522"/><rect x="29" y="14" width="7" height="30" fill="#f26522"/><circle cx="42" cy="8" r="4" fill="none" stroke="#f26522" stroke-width="3"/><circle cx="48" cy="18" r="4" fill="none" stroke="#f26522" stroke-width="3"/><path d="M30 22l10-11M30 22l15-2" stroke="#f26522" stroke-width="3"/></svg>
  </div>
</section>

<section class="gallery">
  <div class="section-title">Video Gallery</div>
  <article class="video-card" style="left:161px">
    <h3>Lorem ipsum dolor sit amet sit almet</h3>
    <div class="video-frame"><div class="video-thumb v1" role="img" aria-label="Video camera filming an outdoor scene with people in soft focus"><span class="play"></span></div></div>
  </article>
  <article class="video-card" style="left:624px">
    <h3>Lorem ipsum dolor sit amet sit almet</h3>
    <div class="video-frame"><div class="video-thumb v2" role="img" aria-label="Film crew with camera and clapperboard on a street set"><span class="play"></span></div></div>
  </article>
  <div class="gallery-dots"><span class="on"></span><span></span><span></span><span></span></div>
</section>

<footer class="site-footer">
  <div class="f-col quick">
    <h4>Quick Links</h4>
    <ul><li>Home</li><li>About Us</li><li>Services</li><li>Video Gallery</li><li>Contact Us</li></ul>
  </div>
  <div class="f-col contact">
    <h4>Contact Details</h4>
    <div class="org">HALBROOK VIDEO</div>
    <div class="addr">123, Lorem ipsum dolor si amet,<br>consectetue nibh euismod</div>
    <div class="row"><svg width="11" height="11" viewBox="0 0 24 24"><path d="M6.6 10.8a15 15 0 006.6 6.6l2.2-2.2 5.6 1.6V21A18 18 0 013 3h4.2l1.6 5.6z" fill="var(--green)"/></svg>(123) 456 7890</div>
    <div class="row"><svg width="9" height="13" viewBox="0 0 9 13"><rect x="1" y="1" width="7" height="11" rx="1" fill="none" stroke="#8cc63f" stroke-width="1.5"/></svg>(123) 456 7890</div>
    <div class="row"><svg width="12" height="9" viewBox="0 0 12 9"><rect x=".5" y=".5" width="11" height="8" fill="#8cc63f"/><path d="M.5 .5l5.5 4.5 5.5-4.5" fill="none" stroke="#242424"/></svg>infor@halbrookvideo.com</div>
  </div>
  <div class="f-col mapcol">
    <h4>Location Map</h4>
    <div class="map" role="img" aria-label="Street map showing the studio location"></div>
  </div>
  <div class="f-brand">
    <div class="mark"></div>
    <div class="name">HALBROOK VIDEO</div>
    <div class="social" aria-label="Social links"><span class="s1"></span><span class="s2"></span><span class="s3"></span><span class="s4"></span></div>
  </div>
</footer>
<div class="copyright">Copyright © 2016 Halbrook Video. All rights reserved.</div>

</body>
</html>
```